Plumbing Service Flyer Needed For Swapnook

Plumbing ad needs to be effective (600 by 450 pixels)
Ad must include company name Kestrel Drainworks and phone number 404-555-0183
No URLs, links, or web addresses in your text or image please.

(about us we offer a wide range of plumbing services from emergency plumbing to commercial plumbing services, our master plumbers are ready to handle all jobs, large or small, at anytime during the day or night. Pickup the phone and call us today).

Target Market(s)

DC Metro Area

Industry/Entity Type

Plumbing

Font styles to use
Other font styles liked:
• No preference. Let the designer choose

Colors

Designer to choose colors to be used in the design.

Requirements
Must have
• 1. A bold headline: headline should communicate what my business is all about.
• 2. Great photography
• 3. Discounts or specials
• 4. Call to action
• 5. Key facts: Let consumers know about the product or service (see attached ad)
• 6. Good graphics
Should not have
• No URLs, links, or web addresses in your text or image please.

```html
<!DOCTYPE html>
<html lang="en">
<head>
<meta charset="utf-8">
<title>Kestrel Drainworks – 24/7 Plumber Flyer</title>
<link rel="stylesheet" href="https://fonts.googleapis.com/css2?family=Oswald:wght@500;600;700&family=Lato:ital,wght@0,400;0,700;1,400;1,700&display=swap">
<style>
  :root {
    --navy: #1f2a5e;
    --navy-deep: #161f4a;
    --yellow: #f7c713;
    --yellow-light: #fbd93a;
    --royal: #1462b4;
    --ink: #1c1c1c;
    --white: #ffffff;
    --stage: #2a2a2a;
  }
  * { margin: 0; padding: 0; box-sizing: border-box; }
  html, body {
    width: 1200px; height: 902px; overflow: hidden;
    background: var(--stage);
  }
  .flyer {
    position: relative; width: 1200px; height: 902px; overflow: hidden;
    background: linear-gradient(160deg, #263370 0%, var(--navy) 55%, var(--navy-deep) 100%);
    font-family: "Lato", Arial, sans-serif; color: var(--white);
  }
  .headline-band {
    position: absolute; left: 0; top: 22px; width: 1200px; height: 128px;
    background: linear-gradient(90deg, var(--yellow) 0%, var(--yellow-light) 50%, var(--yellow) 100%);
  }
  .headline {
    position: absolute; left: 50px; top: 30px; width: 1120px;
    display: flex; align-items: baseline; justify-content: space-between;
    font-family: "Oswald", Impact, sans-serif; font-weight: 700;
    text-transform: uppercase; line-height: 1; white-space: nowrap;
  }
  .headline .what { font-size: 86px; color: var(--ink); }
  .headline .promise {
    font-size: 74px; color: var(--white);
    text-shadow: 0 2px 4px rgba(0,0,0,.35);
  }
  .plumber-photo {
    position: absolute; left: 120px; top: 170px; width: 370px; height: 420px;
    background: radial-gradient(ellipse at 50% 35%, #3d4f8f 0%, #2b3a78 45%, rgba(31,42,94,0) 75%);
  }
  .about {
    position: absolute; left: 440px; top: 175px; width: 690px;
  }
  .section-title {
    font-family: "Oswald", Impact, sans-serif; font-weight: 600;
    color: var(--yellow); text-transform: uppercase; font-size: 20px; letter-spacing: .3px;
  }
  .about p { font-size: 18px; line-height: 1.3; margin-top: 4px; }
  .services { position: absolute; left: 520px; top: 276px; width: 640px; }
  .services .section-title { font-size: 23px; }
  .service-columns { display: flex; gap: 40px; margin-top: 10px; }
  .service-list { list-style: none; }
  .service-list li {
    position: relative; padding-left: 24px; margin-bottom: 6px;
    font-size: 17px; font-style: italic; font-weight: 700; line-height: 1.2;
  }
  .service-list li::before {
    content: ""; position: absolute; left: 0; top: 5px;
    width: 12px; height: 12px; border-radius: 50%; background: var(--yellow);
  }
  .service-list .more {
    padding-left: 24px; color: var(--yellow); font-style: italic; font-weight: 700; font-size: 16px;
  }
  .service-list .more::before { display: none; }
  .waves { position: absolute; left: 0; top: 0; }
  .company {
    position: absolute; left: 64px; top: 560px;
    font-family: "Oswald", Impact, sans-serif; font-weight: 600;
    font-size: 54px; line-height: 1; color: var(--ink); text-transform: uppercase;
  }
  .credentials {
    position: absolute; left: 66px; top: 624px;
    font-size: 18px; font-weight: 700; color: var(--white); text-transform: uppercase; letter-spacing: .3px;
  }
  .cta {
    position: absolute; left: 66px; top: 668px;
    font-family: "Oswald", Impact, sans-serif; font-weight: 600;
    font-size: 32px; color: var(--ink); text-transform: uppercase;
  }
  .phone-row { position: absolute; left: 60px; top: 720px; display: flex; align-items: center; gap: 16px; }
  .phone-number {
    font-family: "Oswald", Impact, sans-serif; font-weight: 700;
    font-size: 84px; line-height: 1; color: var(--white);
    text-shadow: 3px 3px 0 var(--ink), -2px -2px 0 var(--ink), 2px -2px 0 var(--ink), -2px 2px 0 var(--ink), 4px 6px 6px rgba(0,0,0,.4);
  }
  .offer { position: absolute; left: 660px; top: 490px; }
</style>
</head>
<body>
<main class="flyer">
  <div class="headline-band"></div>
  <h1 class="headline"><span class="what">24/7 Plumber</span><span class="promise">At Your Service!</span></h1>

  <div class="plumber-photo" role="img" aria-label="Photo of a smiling plumber in a hard hat and navy overalls holding a pipe wrench"></div>

  <section class="about">
    <h2 class="section-title">About Us</h2>
    <p>we offer a wide range of plumbing services from emergency plumbing to commercial plumbing services, our master plumbers are ready to handle all jobs, large or small, at anytime during the day or night.</p>
  </section>

  <section class="services">
    <h2 class="section-title">Here are a few of my plumbing services:</h2>
    <div class="service-columns">
      <ul class="service-list">
        <li>Plumbing clogs</li>
        <li>Water heater replacement</li>
        <li>Repair and install gas lines</li>
        <li>Remodel your plumbing</li>
        <li>Flood repair</li>
      </ul>
      <ul class="service-list">
        <li>Disposals repair and install</li>
        <li>Toilets install or replace</li>
        <li>New piping and repairs</li>
        <li>New homes, old homes,<br>commercial plumbing</li>
        <li class="more">and a ton more</li>
      </ul>
    </div>
  </section>

  <svg class="waves" width="1200" height="902" viewBox="0 0 1200 902" aria-hidden="true">
    <defs>
      <linearGradient id="yellowFill" x1="0" y1="0" x2="1" y2="1">
        <stop offset="0" stop-color="#f9d22a"/>
        <stop offset="1" stop-color="#f5c20f"/>
      </linearGradient>
    </defs>
    <path d="M0,545 C230,440 470,430 700,570 C860,665 1010,690 1200,678 L1200,902 L0,902 Z" fill="#1462b4"/>
    <path d="M0,565 C230,465 470,455 700,595 C860,690 1010,715 1200,703 L1200,902 L0,902 Z" fill="#ffffff"/>
    <path d="M0,585 C230,488 470,478 700,618 C860,712 1010,735 1200,724" fill="none" stroke="#1c1c1c" stroke-width="8"/>
    <path d="M0,605 C230,508 470,500 700,640 C860,732 1010,755 1200,744 L1200,902 L0,902 Z" fill="#1462b4"/>
    <path d="M0,615 C230,520 470,512 700,652 C860,744 1010,768 1200,758 L1200,840 L0,840 Z" fill="url(#yellowFill)"/>
    <rect x="0" y="840" width="1200" height="8" fill="#ffffff"/>
    <rect x="0" y="848" width="1200" height="54" fill="#1462b4"/>
  </svg>

  <h2 class="company">Kestrel Drainworks</h2>
  <p class="credentials">Bonded, licensed and insured</p>
  <p class="cta">Pickup the phone and call us today</p>
  <div class="phone-row">
    <svg width="60" height="70" viewBox="0 0 60 70" aria-hidden="true">
      <path d="M40,8 A28,28 0 1,0 40,62" fill="none" stroke="#ffffff" stroke-width="6" stroke-linecap="round"/>
      <path d="M14,20 l8,-4 l6,12 l-5,4 q2,8 8,12 l5,-4 l9,10 l-5,6 q-16,-2 -26,-36 z" fill="#ffffff"/>
      <text x="30" y="42" font-family="Lato, Arial, sans-serif" font-size="14" font-weight="700" fill="#ffffff">24</text>
    </svg>
    <span class="phone-number">404-555-0183</span>
  </div>

  <svg class="offer" width="310" height="355" viewBox="0 0 340 390" role="group" aria-label="XX percent off special offer">
    <defs>
      <linearGradient id="silver" x1="0" y1="0" x2="1" y2="0">
        <stop offset="0" stop-color="#9a9a9a"/>
        <stop offset=".45" stop-color="#f4f4f4"/>
        <stop offset=".6" stop-color="#ffffff"/>
        <stop offset="1" stop-color="#8c8c8c"/>
      </linearGradient>
    </defs>
    <path d="M20,40 Q170,0 320,30 L320,250 Q250,330 170,375 Q90,330 20,260 Z" fill="#1462b4"/>
    <path d="M34,50 Q170,14 306,40 L306,244 Q242,316 170,358 Q98,316 34,254 Z" fill="#ffffff"/>
    <path d="M44,58 Q170,26 296,50 L296,238 Q238,304 170,344 Q102,304 44,248 Z" fill="url(#silver)"/>
    <text x="52" y="210" font-family="Oswald, Impact, sans-serif" font-weight="700" font-size="150" fill="#1c1c1c" letter-spacing="-6">XX</text>
    <text x="212" y="130" font-family="Oswald, Impact, sans-serif" font-weight="700" font-size="76" fill="#f7c713">%</text>
    <text x="210" y="190" font-family="Oswald, Impact, sans-serif" font-weight="700" font-size="54" fill="#f7c713">OFF</text>
    <text x="170" y="246" text-anchor="middle" font-family="Oswald, Impact, sans-serif" font-weight="600" font-size="22" fill="#1c1c1c">LOREM IPSUM DUMMY TEXT</text>
  </svg>
</main>
</body>
</html>
```